Business Card Design

We would like to re-design our business cards. Our Company - Qoralin Turbochargers, rebuilds turbochargers and sells replacement parts. Our website is: http://www.qoralinturbochargers-example.com
We just had our logo changed. I will attach the file. Looking for fresh new/modern business card. We like the colors red, black, white and silver. Black background looks attractive, but not a requirement. The final design should communicate reasonable/competitive prices, top quality and reliability of our products.
Updates
Project Deadline Extended
Reason: Need to finalize the info on the card. Currently working on changing address and email info. Want to make sure it is the correct one before accepting the final design. Unless, this is something that can be changed at a later time..??
Industry/Entity Type
Business
Contact Information for Business Card
QORALIN TURBOCHARGERS, LLC
20473 Pemberly Road NE
Massillon, OH 44012
Tel: +1-330-555-0162
Fax: +1-330-555-0187
info@QoralinTurbochargers-example.com
Our current business card had the following highlights:
*We rebuild all Turbocharges for Automotive, Diesel and Industrial
*Precision Balancing and in-house turbocharger needs
*All Turbocharger replacement parts are made in USA / U.K.
Look and feel
Each slider illustrates characteristics of the customer's brand and the style your logo design should communicate.

```html
<!DOCTYPE html>
<html lang="en">
<head>
<meta charset="utf-8">
<title>Qoralin Turbochargers – Business Card</title>
<link rel="stylesheet" href="https://fonts.googleapis.com/css2?family=Roboto:wght@400;500;700;900&display=swap">
<style>
  :root {
    --bg: #e9e7e3;
    --card: #ffffff;
    --red: #e8262b;
    --ink: #1e1e1e;
    --shadow: rgba(0, 0, 0, 0.18);
  }
  * { margin: 0; padding: 0; box-sizing: border-box; }
  html, body { width: 1200px; height: 892px; overflow: hidden; }
  body {
    background: var(--bg);
    font-family: "Roboto", Arial, sans-serif;
    color: var(--ink);
    position: relative;
  }
  .card {
    position: absolute;
    width: 700px;
    height: 400px;
    background: var(--card);
    box-shadow: 0 6px 18px var(--shadow);
  }
  .card-back { left: 440px; top: 36px; }
  .card-front { left: 60px; top: 456px; }

  .brand {
    display: flex;
    align-items: center;
    gap: 14px;
  }
  .brand-mark {
    width: 34px;
    height: 34px;
    background: var(--red);
    flex: none;
  }
  .brand-name {
    font-weight: 900;
    color: var(--ink);
    white-space: nowrap;
    letter-spacing: 0.5px;
  }
  .card-back .brand {
    position: absolute;
    left: 0; right: 0; top: 168px;
    justify-content: center;
  }
  .card-back .brand-mark { width: 50px; height: 50px; }
  .card-back .brand-name { font-size: 40px; }

  .card-front .brand {
    position: absolute;
    left: 110px; top: 40px;
  }
  .card-front .brand-mark { width: 40px; height: 40px; }
  .card-front .brand-name { font-size: 32px; }

  .person {
    position: absolute;
    left: 70px; top: 112px;
  }
  .person-name {
    font-size: 44px;
    font-weight: 500;
    color: var(--red);
    line-height: 1;
  }
  .person-role {
    font-size: 15px;
    font-weight: 700;
    margin-top: 8px;
  }

  .contact-list {
    position: absolute;
    left: 70px; top: 222px;
    list-style: none;
  }
  .contact-list li {
    display: flex;
    align-items: center;
    gap: 14px;
    font-size: 20px;
    line-height: 30px;
    white-space: nowrap;
  }
  .contact-icon {
    width: 17px; height: 17px;
    flex: none;
  }
</style>
</head>
<body>

<section class="card card-back">
  <div class="brand">
    <span class="brand-mark"></span>
    <span class="brand-name">Qoralin Turbochargers</span>
  </div>
</section>

<section class="card card-front">
  <div class="brand">
    <span class="brand-mark"></span>
    <span class="brand-name">Qoralin Turbochargers</span>
  </div>

  <div class="person">
    <p class="person-name">Employee name</p>
    <p class="person-role">Managing Director</p>
  </div>

  <ul class="contact-list">
    <li>
      <svg class="contact-icon" viewBox="0 0 16 16" aria-hidden="true">
        <rect width="16" height="16" rx="2" fill="#e8262b"/>
        <path d="M5 3.5l1.8 2-1 1.2c.6 1.4 1.6 2.4 3 3l1.2-1 2 1.8-1 1.6c-3.6-.3-6.6-3.3-6.9-6.9z" fill="#fff"/>
      </svg>
      <span>555-555-0162</span>
    </li>
    <li>
      <svg class="contact-icon" viewBox="0 0 16 16" aria-hidden="true">
        <rect width="16" height="16" rx="2" fill="#e8262b"/>
        <circle cx="8" cy="8" r="4.5" fill="none" stroke="#fff" stroke-width="1.3"/>
        <path d="M3.5 8h9M8 3.5c-2 2.5-2 6.5 0 9M8 3.5c2 2.5 2 6.5 0 9" fill="none" stroke="#fff" stroke-width="1"/>
      </svg>
      <span>www.qoralinturbochargers-example.com</span>
    </li>
    <li>
      <svg class="contact-icon" viewBox="0 0 16 16" aria-hidden="true">
        <rect width="16" height="16" rx="2" fill="#e8262b"/>
        <rect x="3" y="4.5" width="10" height="7" fill="none" stroke="#fff" stroke-width="1.2"/>
        <path d="M3 4.5l5 4 5-4" fill="none" stroke="#fff" stroke-width="1.2"/>
      </svg>
      <span>info@QoralinTurbochargers-example.com</span>
    </li>
    <li>
      <svg class="contact-icon" viewBox="0 0 16 16" aria-hidden="true">
        <rect width="16" height="16" rx="2" fill="#e8262b"/>
        <path d="M8 13s-3.5-3.6-3.5-6.2a3.5 3.5 0 0 1 7 0C11.5 9.4 8 13 8 13z" fill="#fff"/>
        <circle cx="8" cy="6.8" r="1.3" fill="#e8262b"/>
      </svg>
      <span>4182 Harwick Ave. NW Brenford Falls, Westland</span>
    </li>
  </ul>
</section>

</body>
</html>
```